Gruppo Abitativo Sorena
complete stationary set
Gruppo Abitativo Sorena - Real Estate
Creative Brief
Professional
Marcello Ruffoni
Responsabile di agenzia
Gruppo Abitativo Sorena Via Castellana, 147 20384 Milano - Italy
marcello.ruffoni@gruppoabitativosorena.example
www.gruppoabitativosorena.example
I'm looking for a complete set of stationary: 1. Business Cards 2. Letter Head 3. Presentation Folder 6. Envelopes 7. PowerPoint slide template 9. Note pad cover 10. e-mail signature 11. Fax Cover Please insert QR Code and a photo box in business card. For further information post comments or contact me I will give you all feedback you need
Should have something to that represents our company and will make them want to look at the card again.

```html
<!DOCTYPE html>
<html lang="it">
<head>
<meta charset="utf-8">
<title>Gruppo Abitativo Sorena – Biglietto da visita</title>
<link href="https://fonts.googleapis.com/css2?family=Open+Sans:wght@400;600;700;800&display=swap" rel="stylesheet">
<style>
  :root {
    --bg: #e9e7e4;
    --card-white: #ffffff;
    --navy: #1b2a78;
    --navy-deep: #0d1550;
    --navy-light: #2f46b0;
    --swoosh: #b9bcc4;
    --text-grey: #8a8d94;
    --photo: #e6e7ea;
    --white: #ffffff;
  }
  * { box-sizing: border-box; margin: 0; padding: 0; }
  html, body {
    width: 1200px; height: 780px; overflow: hidden;
    background: var(--bg);
    font-family: "Open Sans", Arial, sans-serif;
  }
  .business-card {
    position: absolute; left: 100px; top: 90px;
    width: 1000px; height: 600px;
    border-radius: 36px; overflow: hidden;
    background: var(--card-white);
    box-shadow: 0 10px 30px rgba(0,0,0,.18);
  }
  .card-wave { position: absolute; inset: 0; width: 100%; height: 100%; }
  .brand { position: absolute; left: 60px; top: 70px; }
  .brand-name {
    display: flex; align-items: center; gap: 10px;
    font-weight: 800; font-size: 24px; letter-spacing: .3px;
    color: var(--navy); text-transform: uppercase; white-space: nowrap;
  }
  .brand-square { width: 20px; height: 20px; background: var(--navy); flex: none; }
  .brand-web {
    margin-top: 4px; font-size: 13px; letter-spacing: 1.6px;
    color: var(--text-grey);
  }
  .photo-box {
    position: absolute; left: 72px; top: 190px;
    width: 220px; height: 220px;
    background: var(--photo); border: 2px solid #dcdde1;
  }
  .holder { position: absolute; left: 64px; top: 450px; }
  .holder-name { font-size: 34px; font-weight: 700; color: var(--navy); }
  .holder-role { font-size: 23px; color: var(--text-grey); margin-top: 2px; }
  .company-address {
    position: absolute; left: 620px; top: 120px;
    color: var(--white); font-size: 22px; line-height: 1.35; font-style: normal;
  }
  .contact-list {
    position: absolute; right: 48px; top: 318px;
    list-style: none; color: var(--white); font-size: 22px;
  }
  .contact-list li {
    display: flex; align-items: center; justify-content: flex-end;
    gap: 14px; height: 34px;
  }
  .contact-list svg { width: 22px; height: 22px; fill: var(--white); }
  .contact-email {
    position: absolute; right: 48px; bottom: 62px;
    display: flex; align-items: center; gap: 10px;
    color: var(--white); font-size: 14px; white-space: nowrap;
  }
  .at-sign { font-size: 24px; font-weight: 700; line-height: 1; }
</style>
</head>
<body>
  <div class="business-card">
    <svg class="card-wave" viewBox="0 0 1000 600" preserveAspectRatio="none" aria-hidden="true">
      <defs>
        <radialGradient id="navyGlow" cx="0.55" cy="0.42" r="0.7">
          <stop offset="0" stop-color="#2f46b0"/>
          <stop offset="0.55" stop-color="#1b2a78"/>
          <stop offset="1" stop-color="#0d1550"/>
        </radialGradient>
      </defs>
      <path d="M545,-10 C620,110 520,230 540,330 C560,430 520,520 470,610" fill="none" stroke="var(--swoosh)" stroke-width="14"/>
      <path d="M580,0 C650,120 555,230 575,330 C595,430 555,530 500,600 L1000,600 L1000,0 Z" fill="url(#navyGlow)"/>
    </svg>

    <div class="brand">
      <div class="brand-name">Gruppo Abitativo Sorena <span class="brand-square"></span></div>
      <div class="brand-web">www.gruppoabitativosorena.example</div>
    </div>

    <div class="photo-box" role="img" aria-label="Spazio per la foto del titolare"></div>

    <div class="holder">
      <div class="holder-name">Marcello Ruffoni</div>
      <div class="holder-role">Responsabile di agenzia</div>
    </div>

    <address class="company-address">
      Gruppo Abitativo Sorena<br>
      Via Castellana, 147<br>
      20384 Milano - Italy
    </address>

    <ul class="contact-list">
      <li>+39 00 00 00 000
        <svg viewBox="0 0 24 24" aria-label="Telefono"><path d="M6.6 10.8a15 15 0 0 0 6.6 6.6l2.2-2.2a1 1 0 0 1 1-.25 11.4 11.4 0 0 0 3.6.57 1 1 0 0 1 1 1V20a1 1 0 0 1-1 1A17 17 0 0 1 3 4a1 1 0 0 1 1-1h3.5a1 1 0 0 1 1 1c0 1.25.2 2.45.57 3.57a1 1 0 0 1-.25 1z"/></svg>
      </li>
      <li>+39 111 22 33 456
        <svg viewBox="0 0 24 24" aria-label="Fax"><path d="M7 2h8l3 3v5H7z M4 11h16a2 2 0 0 1 2 2v7H2v-7a2 2 0 0 1 2-2z M6 14v2h3v-2z M11 14v2h3v-2z"/></svg>
      </li>
      <li>+39 12 34 56 789
        <svg viewBox="0 0 24 24" aria-label="Cellulare"><path d="M8 1h8a2 2 0 0 1 2 2v18a2 2 0 0 1-2 2H8a2 2 0 0 1-2-2V3a2 2 0 0 1 2-2zm0 3v14h8V4zm4 15.5a1 1 0 1 0 0 2 1 1 0 0 0 0-2z"/></svg>
      </li>
    </ul>

    <div class="contact-email">
      marcello.ruffoni@gruppoabitativosorena.example
      <span class="at-sign">@</span>
    </div>
  </div>
</body>
</html>
```